Law Firm Website, easily updated by User

We are a regional Labor and Employment Law Firm with a tired outdated website. We are looking for a clean easy to use website that will allow us to easily update information and articles in house. Our current website can be found at www.quillbarrowfirm.com

Industry/Entity Type

Labor

Number of Pages Required

5+ page

Colors
0655a3

Requirements
Must have
• Content easily updated by user
Nice to have
• crisp clean pages
Should not have
• stock pictures

```html
<!DOCTYPE html>
<html lang="en">
<head>
<meta charset="utf-8">
<title>Quillbarrow Law, P.C.</title>
<link rel="stylesheet" href="https://fonts.googleapis.com/css2?family=Lato:wght@400;700&display=swap">
<style>
  :root {
    --brand-blue: #0a6db5;
    --light-blue: #5cc0f0;
    --charcoal: #555555;
    --ink: #333333;
    --panel: #e8e8e8;
    --tile: #c9c9c9;
    --tile-edge: #b5b5b5;
    --white: #ffffff;
  }
  * { box-sizing: border-box; margin: 0; padding: 0; }
  html, body { width: 1200px; height: 900px; overflow: hidden; background: var(--white); }
  body { font-family: "Lato", sans-serif; color: var(--ink); position: relative; }
  .page { position: absolute; left: 225px; top: 0; width: 749px; height: 900px; }

  .site-header { position: absolute; left: 0; top: 0; width: 749px; height: 94px; background: var(--charcoal); color: var(--white); }
  .firm-name { position: absolute; left: 120px; top: 34px; font-size: 25px; font-weight: 400; letter-spacing: 0.2px; white-space: nowrap; }
  .consult { position: absolute; left: 500px; top: 18px; width: 140px; text-align: center; font-size: 10.5px; line-height: 13px; }
  .consult .call { font-size: 9px; }
  .consult .call b { color: var(--light-blue); font-weight: 400; font-size: 10px; }

  .main-nav { position: absolute; left: 0; top: 94px; width: 749px; height: 26px; display: flex; justify-content: center; align-items: center; font-size: 9.5px; font-weight: 700; color: #111; }
  .main-nav a { color: inherit; text-decoration: none; }
  .main-nav a.current { color: var(--brand-blue); font-weight: 400; }
  .main-nav .sep { margin: 0 12px; font-weight: 400; }
  .main-nav .sep.tight { margin: 0 9px 0 5px; }

  .hero { position: absolute; left: 0; top: 120px; width: 749px; height: 203px; }
  .hero-photo { position: absolute; inset: 0; background: linear-gradient(100deg, #b9bcbf 0%, #dadcdd 35%, #cfd1d2 60%, #e4e5e6 100%); }
  .hero-title { position: absolute; left: 0; top: 53px; width: 749px; text-align: center; font-size: 25px; line-height: 25px; font-weight: 400; color: var(--ink); }
  .hero-title em { font-style: normal; color: var(--brand-blue); }

  .section-title { position: absolute; left: 0; width: 749px; text-align: center; font-size: 19px; font-weight: 400; color: var(--brand-blue); }
  .section-title .amp { color: #111; }
  .attorneys-title { top: 339px; padding-right: 16px; }
  .attorney-card { position: absolute; top: 373px; width: 156px; height: 156px; background: var(--tile); border: 1px solid var(--tile-edge); display: flex; align-items: center; justify-content: center; font-size: 15px; color: #444; padding-bottom: 4px; }

  .credentials { position: absolute; left: 0; top: 539px; width: 749px; height: 206px; background: var(--panel); }
  .credentials .section-title { top: 28px; padding-left: 32px; }
  .cred-list { position: absolute; top: 70px; list-style: none; font-size: 10.5px; line-height: 15.6px; letter-spacing: 0.5px; color: #333; }
  .cred-list.admissions { left: 130px; width: 250px; }
  .cred-list.associations { left: 409px; width: 240px; }

  .site-footer { position: absolute; left: 0; top: 745px; width: 749px; height: 155px; background: var(--charcoal); color: var(--white); }
  .footer-links { position: absolute; top: 47px; list-style: none; font-size: 9.5px; line-height: 15.7px; letter-spacing: 0.5px; }
  .footer-links a { color: inherit; text-decoration: none; }
  .footer-links.col-a { left: 130px; }
  .footer-links.col-b { left: 213px; top: 48px; }
  .footer-contact { position: absolute; right: 122px; top: 45px; text-align: right; font-size: 11px; line-height: 13.3px; letter-spacing: 0.5px; }
  .legal { position: absolute; left: 0; top: 129px; width: 749px; text-align: center; font-size: 7px; line-height: 12px; }
</style>
</head>
<body>
<div class="page">
  <header class="site-header">
    <div class="firm-name">QUILLBARROW LAW, P.C.</div>
    <div class="consult">
      <div>For a Free Consultation</div>
      <div class="call"><b>Call:</b> (555) 214-7730</div>
    </div>
  </header>

  <nav class="main-nav">
    <a class="current" href="#">Home</a><span class="sep">|</span>
    <a href="#">About Us</a><span class="sep">|</span>
    <a href="#">Pratice Area</a><span class="sep">|</span>
    <a href="#">In the News</a><span class="sep">|</span>
    <a href="#">FAQ</a><span class="sep tight">|</span>
    <a href="#">For Employers</a><span class="sep">|</span>
    <a href="#">Contact us</a>
  </nav>

  <section class="hero">
    <div class="hero-photo" role="img" aria-label="Faded photograph of a row of stone balusters along a walkway"></div>
    <h1 class="hero-title"><em>Counselling</em> and <em>Advising</em> Clients<br>Exclusively on Laws of the Workplace</h1>
  </section>

  <h2 class="section-title attorneys-title">Our Attorneys</h2>
  <div class="attorney-card" style="left:120px">Img</div>
  <div class="attorney-card" style="left:296px">Img</div>
  <div class="attorney-card" style="left:473px">Img</div>

  <section class="credentials">
    <h2 class="section-title">Admissions <span class="amp">&amp;</span> Associations</h2>
    <ul class="cred-list admissions">
      <li>New York State</li>
      <li>Eastern District of New York</li>
      <li>Southern District of New York</li>
      <li>United States Court of Appeals for the Second Circuit</li>
      <li>United States Court of Federal Claims</li>
    </ul>
    <ul class="cred-list associations">
      <li>Greystone State Bar Association</li>
      <li>Marlow County Bar Association</li>
      <li>Ashford County Bar Association</li>
      <li>Allied Trial Counsel Association</li>
      <li>Guild of Workplace Law Advocates</li>
    </ul>
  </section>

  <footer class="site-footer">
    <ul class="footer-links col-a">
      <li><a href="#">Home</a></li>
      <li><a href="#">About Us</a></li>
      <li><a href="#">Practice Area</a></li>
      <li><a href="#">In the News</a></li>
    </ul>
    <ul class="footer-links col-b">
      <li><a href="#">FAQ</a></li>
      <li><a href="#">For Employers</a></li>
      <li><a href="#">Contact Us</a></li>
    </ul>
    <div class="footer-contact">
      <div>Phone: (555) 214 7730</div>
      <div>Facesimile: (555) 214 7731</div>
      <div>Email: info@quillbarrowfirm.com</div>
    </div>
    <div class="legal">
      <div>Copyright © 2013. All Rights Reserved. Quillbarrow Law, P.C.</div>
      <div>Privacy Policy | Disclaimer</div>
    </div>
  </footer>
</div>
</body>
</html>
```